Research campaign for the global health issues in Africa must be modern, impactful and unique *

Please see attachment
Research campaign for the global health issues in Africa must be modern, impactful and unique
Updates

Please find the updated flyer requirement. These designs are not modern. We would need this flyer displayed on PV , Chatterloop and blurtwave. Please use either option of the requirement. Color scheme is Blue.

Target Market(s)

Patients, volunteers, patient advocacy groups, hospitals, healthcare professionals

Industry/Entity Type

Health Care

Font styles to use
Serif

Colors
0355a3
fbed22
f04a50

Requirements
Must have
• Please note that this must be a modern flyer that can be posted on Pictavine so size matters here.
Nice to have
• To see African/black people or foot print or shadow of a walk
• There can be a background image of a child’s face or Person walking or We could have a hand print or foot print with different disease colors.

```html
<!DOCTYPE html>
<html lang="en">
<head>
<meta charset="utf-8">
<title>Walk for Global Health Research Campaign 2019 – Flyer</title>
<link rel="stylesheet" href="https://fonts.googleapis.com/css2?family=Montserrat:wght@300;700&family=Open+Sans:ital,wght@0,400;0,600;0,700;1,400&display=swap">
<style>
  :root{
    --stage:#bcd9f0;
    --brand-blue:#1174c4;
    --deep-blue:#0f5fa8;
    --paper:#ffffff;
    --panel-grey:#e6e7ea;
    --ink:#3a3f45;
    --heading-blue:#1572bf;
  }
  *{margin:0;padding:0;box-sizing:border-box}
  html,body{width:1200px;height:886px;overflow:hidden;background:var(--stage)}
  body{position:relative;font-family:"Open Sans",Arial,sans-serif;color:var(--ink)}

  .page{position:absolute;top:92px;width:486px;height:688px;background:var(--paper);overflow:hidden;
        box-shadow:0 2px 4px rgba(0,0,0,.25)}
  .page--front{left:88px}
  .page--back{left:604px}

  /* front */
  .front__photo{position:absolute;left:36px;top:90px;width:400px;height:323px;
        background:radial-gradient(circle at 78% 55%,#8fc4ea 0 18%,transparent 19%),
                   linear-gradient(160deg,#f3ece6 0%,#c98d70 30%,#8fbde2 60%,#cfe3f4 100%);
        border-radius:4px 4px 0 0}
  .date-card{position:absolute;left:280px;top:0;width:130px;height:222px;background:var(--brand-blue);
        color:#fff;padding:72px 12px 0 12px;font-size:12.5px;line-height:15.5px}
  .date-card__label{font-weight:700;font-size:16px;line-height:20px;padding-bottom:2px;border-bottom:1px solid #fff;margin-bottom:8px}
  .date-card__venue{border-bottom:1px solid #fff;padding-bottom:4px;margin-bottom:6px}
  .date-card em{font-style:italic}
  .date-card strong{font-weight:700}
  .date-card__fold{position:absolute;left:410px;top:157px}

  .front__band{position:absolute;left:0;top:413px;width:486px;height:164px;background:var(--brand-blue);
        color:#fff;padding:19px 0 0 42px;font-family:"Montserrat",Arial,sans-serif;font-weight:300;
        font-size:25px;line-height:33px;letter-spacing:.5px;white-space:nowrap}
  .front__band b{font-weight:700;letter-spacing:0}
  .back__title b{font-weight:700}

  .front__info{position:absolute;left:0;top:577px;width:486px;height:91px;background:var(--panel-grey);padding:18px 0 0 46px}
  .service{display:flex;align-items:center;gap:8px;font-size:12.5px;color:#444}
  .service svg{flex:none}
  .mission{margin-top:10px;font-size:8.3px;line-height:11px;font-weight:600;color:#333;width:410px}

  .page__strip{position:absolute;left:0;bottom:0;width:486px;height:20px;background:var(--brand-blue)}

  /* back */
  .back__hero{position:absolute;left:0;top:0;width:486px;height:448px;
        background:radial-gradient(circle at 70% 52%,#2c7ac4 0 26%,transparent 27%),
                   linear-gradient(135deg,#1a6cbc 0%,#1f74c2 50%,#1c6db9 100%)}
  .back__title{position:absolute;left:42px;top:42px;color:#fff;font-family:"Montserrat",Arial,sans-serif;
        font-weight:300;font-size:31.5px;line-height:41.8px;letter-spacing:0;white-space:nowrap}
  .back__info{position:absolute;left:0;top:448px;width:486px;height:220px;background:var(--panel-grey);padding:34px 0 0 65px}
  .benefits__lead{color:var(--heading-blue);font-weight:600;font-size:13.5px;line-height:17px;width:360px}
  .benefits{list-style:none;margin-top:17px}
  .benefits li{position:relative;padding-left:10px;font-size:8.6px;line-height:10.5px;font-weight:600;color:#333;margin-bottom:12.5px}
  .benefits li::before{content:"";position:absolute;left:-1px;top:2px;width:5px;height:5px;
        border-right:1.6px solid var(--heading-blue);border-top:1.6px solid var(--heading-blue);transform:rotate(45deg)}
</style>
</head>
<body>

<section class="page page--front">
  <div class="front__photo" role="img" aria-label="Nurse in blue scrubs listening to an inflatable world globe with a red stethoscope"></div>

  <div class="date-card">
    <div class="date-card__label">Date:</div>
    <div class="date-card__venue">
      <em>Saturday,</em><br>
      <strong>May 25, 2019</strong><br>
      OKTH (Lanre-Ese)<br>
      Gate to <strong>Civic<br>Stadium Orelu</strong>
    </div>
    <div><em>Time:</em> <strong>7:00 am</strong></div>
  </div>
  <svg class="date-card__fold" width="16" height="65" viewBox="0 0 16 65"><polygon points="0,0 16,0 4,65 0,65" fill="#8d8f93"/></svg>

  <div class="front__band">
    WALK FOR GLOBAL HEALTH<br>
    RESEARCH CAMPAIGN 2019<br>
    IN COMMEMORATION OF <b>THE</b><br>
    <b>WORLD CLINICAL TRIALS DAY</b>
  </div>

  <div class="front__info">
    <div class="service">
      <svg width="26" height="20" viewBox="0 0 26 20" fill="none" stroke="#1572bf" stroke-width="1.3">
        <circle cx="15" cy="6" r="5"/><path d="M15 3.5v5M12.5 6h5"/>
        <path d="M1 12h5v7H1z"/><path d="M6 13h6l3 2h7l3-2v2l-5 4H6"/>
      </svg>
      free health screening and consultation
    </div>
    <p class="mission">#WFGHRC2019Veltrane Research is committed to finding innovative global health solutions through clinical research</p>
  </div>
  <div class="page__strip"></div>
</section>

<section class="page page--back">
  <div class="back__hero" role="img" aria-label="Child holding a world globe in front of a brick wall, tinted blue"></div>
  <h1 class="back__title">
    WALK<br>FOR GLOBAL<br>HEALTH<br>RESEARCH<br>CAMPAIGN 2019<br>IN COMMEMORATION<br>OF <b>THE WORLD</b><br><b>CLINICAL</b><br><b>TRIALS DAY</b>
  </h1>

  <div class="back__info">
    <p class="benefits__lead">The potential benefits of participating in a clinical trial may include the following:</p>
    <ul class="benefits">
      <li>Access to promising new treatments often not available outside the clinical-trial setting</li>
      <li>Treatment that may be more effective than the standard approach</li>
      <li>The opportunity to be the first to benefit from a new method under study</li>
      <li>The chance to play an active role in your own health care and gain<br>a greater understanding of your disease or condition</li>
    </ul>
  </div>
  <div class="page__strip"></div>
</section>

</body>
</html>
```